Infectious Diseases Research Laboratory Needs Business Card

We need a business card for an academic research laboratory based in Kansas City called MORVEK. The full lab name is Microbial Dose-Response/Exposure Bridging Studies Laboratory, but this does not need to be incorporated. We study novel ways to optimize the treatment of multidrug-resistant bacterial infections ("superbugs") throughout the entire biomedical research spectrum (from benchtop to bedside). The name MORVEK is not only an acronym for our lab name, but also represents our desire to make discoveries and explore the unknown (the stars, if you well). It also serves as an ode to the state of Kansas motto where we are based, ad astra per aspera ("to the stars, through difficulty").

Target Market(s)

Pharmaceutical companies, researchers

Industry/Entity Type

Pharmaceutical

Contact Information for Business Card

The business card should incorporate and complement our new logo (see uploaded files). Double-sided designs are preferred. Looking for something modern, but professional.

Font styles to use
Sans Serif

Requirements
Must have
• Double-sided. One side would ideally be a solid color incorporating logo and the other should also have the logo (smaller), but incorporate staff information.
• Color codes:
• Red: #F04C51
• Blue: #3477B5
• Gray: #808285

```html
<!DOCTYPE html>
<html lang="en">
<head>
<meta charset="utf-8">
<title>MORVEK Business Card</title>
<link href="https://fonts.googleapis.com/css2?family=Roboto:wght@400;500&family=Roboto+Condensed:wght@700&display=swap" rel="stylesheet">
<style>
  :root {
    --red: #F04C51;
    --blue: #3477B5;
    --gray: #808285;
    --card: #202022;
    --card-edge: #2a2a2d;
    --stage: #3b3b3e;
    --ink: #f2f2f2;
  }
  * { margin: 0; padding: 0; box-sizing: border-box; }
  html, body {
    width: 1200px; height: 900px; overflow: hidden;
    background: var(--stage);
    font-family: "Roboto", Arial, sans-serif;
  }
  .card {
    position: absolute; left: 240px;
    width: 720px; height: 400px;
    background: linear-gradient(160deg, var(--card-edge), var(--card) 60%);
    border-radius: 4px;
    box-shadow: 0 14px 30px rgba(0,0,0,.45);
    color: var(--ink);
  }
  .card--front { top: 35px; }
  .card--back { top: 465px; }

  .wordmark {
    position: absolute; left: 0; right: 0; top: 150px;
    display: flex; justify-content: center; align-items: center; gap: 20px;
  }
  .wordmark__dot {
    width: 58px; height: 58px; border-radius: 50%;
    background: var(--blue);
  }
  .wordmark__name {
    font-family: "Roboto", Arial, sans-serif;
    font-weight: 500; font-size: 62px; letter-spacing: 8px;
    color: var(--red);
  }
  .website {
    position: absolute; left: 0; right: 0; top: 282px;
    text-align: center; font-size: 15px; letter-spacing: 9px;
    color: var(--ink);
  }

  .identity {
    position: absolute; right: 400px; top: 115px; text-align: right;
  }
  .identity__name {
    font-family: "Roboto Condensed", "Arial Narrow", sans-serif;
    font-weight: 700; font-size: 38px; color: var(--blue); line-height: 1;
  }
  .identity__title {
    font-family: "Roboto Condensed", "Arial Narrow", sans-serif;
    font-weight: 700; font-size: 18px; color: var(--red);
    margin-top: 8px; letter-spacing: .5px;
  }
  .divider {
    position: absolute; left: 342px; top: 85px;
    width: 2px; height: 120px;
    background: linear-gradient(to bottom, transparent, var(--gray) 30%, #cfcfcf 60%, transparent);
  }
  .contacts {
    position: absolute; left: 372px; top: 88px; list-style: none;
  }
  .contacts li {
    display: flex; align-items: center; gap: 12px;
    font-size: 18px; line-height: 23px; font-weight: 500;
  }
  .contacts svg, .address svg { fill: var(--blue); flex: none; }
  .address {
    position: absolute; left: 70px; top: 298px;
    display: flex; align-items: center; gap: 6px;
    font-size: 19px; font-weight: 500;
  }
</style>
</head>
<body>
  <section class="card card--front" aria-label="Card front">
    <div class="wordmark">
      <span class="wordmark__dot"></span>
      <span class="wordmark__name">MORVEK</span>
    </div>
    <p class="website">www.morvek.com</p>
  </section>

  <section class="card card--back" aria-label="Card back">
    <div class="identity">
      <h1 class="identity__name">DANA KELLER</h1>
      <p class="identity__title">CEO/FOUNDER</p>
    </div>
    <span class="divider"></span>
    <ul class="contacts">
      <li><svg width="14" height="14" viewBox="0 0 24 24"><path d="M6.6 10.8a15.1 15.1 0 0 0 6.6 6.6l2.2-2.2a1 1 0 0 1 1-.25 11.4 11.4 0 0 0 3.6.57 1 1 0 0 1 1 1V20a1 1 0 0 1-1 1A17 17 0 0 1 3 4a1 1 0 0 1 1-1h3.5a1 1 0 0 1 1 1c0 1.25.2 2.45.57 3.57a1 1 0 0 1-.25 1z"/></svg>816 555 0142</li>
      <li><svg width="14" height="14" viewBox="0 0 24 24"><path d="M7 1h10a2 2 0 0 1 2 2v18a2 2 0 0 1-2 2H7a2 2 0 0 1-2-2V3a2 2 0 0 1 2-2zm0 3v14h10V4zm5 15.5a1 1 0 1 0 0 2 1 1 0 0 0 0-2z"/></svg>816 555 0187</li>
      <li><svg width="14" height="14" viewBox="0 0 24 24"><path d="M6 2h12v5H6zM4 8h16a2 2 0 0 1 2 2v7h-4v5H6v-5H2v-7a2 2 0 0 1 2-2zm4 7v5h8v-5z"/></svg>816 555 0199</li>
      <li><svg width="14" height="14" viewBox="0 0 24 24"><path d="M2 5h20v14H2zm2 2v.5l8 5 8-5V7z"/></svg>dkeller@morvek.org</li>
      <li><svg width="14" height="14" viewBox="0 0 24 24"><path d="M12 2a10 10 0 1 0 0 20 10 10 0 0 0 0-20zm-1 17.9A8 8 0 0 1 4.2 10.8L9 15.6v1a2 2 0 0 0 2 2zm6.9-2.5a2 2 0 0 0-1.9-1.4h-1v-3a1 1 0 0 0-1-1H8v-2h2a1 1 0 0 0 1-1V7h2a2 2 0 0 0 2-2v-.4a8 8 0 0 1 2.9 12.8z"/></svg>www.morvek.org</li>
    </ul>
    <p class="address"><svg width="14" height="20" viewBox="0 0 24 34"><path d="M12 0a12 12 0 0 0-12 12c0 9 12 22 12 22s12-13 12-22A12 12 0 0 0 12 0zm0 17a5 5 0 1 1 0-10 5 5 0 0 1 0 10z"/></svg>4120 Linden Court, Kansas City, Kansas 66160</p>
  </section>
</body>
</html>
```